Cleaning Company needs a new business card design

Hi, We are looking for new business card designs to update with our latest logo and company information.
We would like to see designs using the colours:
Royal Blue #4169E1 - this is our company colour so this has to be in there. Please feel free to experiment with other colours.
Must include:
Front of business card:
Logo
Back of the business card:
0800 529 6081
07438 915 702
Email: info@pkrtidyhomes.co.uk
Web: www.pkrtidyhomes.co.uk
Services:
End of Tenancy
Carpet & Upholstery
Regular & One Off
all work fully insured.
The front of the business card with the logo can be made to look raised print. The blue man to be a shiny finish.
The business card needs to be presented in a matt finish
The business must be in the following styles:
Standard Square with rounded corners.
Thank you to all that take part in this.
Target Market(s)
Men and Women of different ages in the UK.
Industry/Entity Type
House Cleaning
Contact Information for Business Card
Front of business card:
Logo
0800 529 6081
07438 915 702
Email: pkrtidy@mailbox-demo.co.uk
Services:
End of Tenancy
Carpet & Upholstery
Regular & One Off
all work fully insured.

```html
<!DOCTYPE html>
<html lang="en">
<head>
<meta charset="utf-8">
<title>PKR Tidy Homes – Business Card</title>
<link rel="stylesheet" href="https://fonts.googleapis.com/css2?family=Open+Sans:wght@400;600;700;800&display=swap">
<style>
  :root {
    --royal: #2e4aa3;
    --royal-deep: #28428f;
    --ink: #1d1d1f;
    --paper: #ffffff;
    --canvas: #ffffff;
    --hairline: #3a3a3a;
  }
  * { box-sizing: border-box; margin: 0; padding: 0; }
  html, body {
    width: 1050px;
    height: 1200px;
    overflow: hidden;
    background: var(--canvas);
    font-family: "Open Sans", Arial, sans-serif;
  }
  .sheet {
    position: relative;
    width: 1050px;
    height: 1200px;
  }
  .card {
    position: absolute;
    left: 157px;
    width: 736px;
    height: 426px;
    overflow: hidden;
  }

  /* Front */
  .card--front {
    top: 124px;
    background: var(--royal);
  }
  .front-pattern {
    position: absolute;
    inset: 0;
    background: radial-gradient(ellipse at center, var(--royal) 0%, var(--royal-deep) 100%);
  }
  .front-wordmark {
    position: absolute;
    left: 0;
    right: 0;
    top: 138px;
    text-align: center;
    color: var(--paper);
    font-weight: 700;
    line-height: 1.1;
  }
  .front-wordmark .name {
    display: block;
    font-size: 64px;
    letter-spacing: -1px;
  }
  .front-wordmark .suffix {
    display: block;
    font-size: 32px;
    margin-top: 6px;
  }

  /* Back */
  .card--back {
    top: 649px;
    background: var(--paper);
    border: 1.5px solid var(--hairline);
  }
  .back-shape {
    position: absolute;
    inset: 0;
    width: 100%;
    height: 100%;
  }
  .back-shape path { fill: var(--royal); }
  .get-in-touch {
    position: absolute;
    left: 19px;
    top: 184px;
    color: var(--paper);
    font-size: 34px;
    font-weight: 700;
    letter-spacing: 0.3px;
  }
  .services {
    position: absolute;
    left: 21px;
    top: 244px;
    list-style: none;
    color: var(--paper);
    font-size: 15px;
    line-height: 23px;
  }
  .services li::before {
    content: "";
    display: inline-block;
    width: 6px;
    height: 6px;
    margin: 0 9px 2px 0;
    border-radius: 50%;
    background: var(--paper);
  }
  .services .insured {
    font-style: italic;
  }
  .back-wordmark {
    position: absolute;
    right: 36px;
    top: 62px;
    text-align: center;
    color: var(--royal);
    font-weight: 800;
    line-height: 1.05;
  }
  .back-wordmark .name {
    display: block;
    font-size: 30px;
    letter-spacing: -0.5px;
  }
  .back-wordmark .suffix {
    display: block;
    font-size: 15px;
    margin-top: 2px;
  }
  .contact-list {
    position: absolute;
    left: 346px;
    top: 248px;
    list-style: none;
    color: var(--ink);
    font-size: 20.5px;
    line-height: 33px;
  }
  .website {
    position: absolute;
    left: 308px;
    top: 379px;
    color: var(--paper);
    font-size: 22px;
    letter-spacing: 0.2px;
  }
</style>
</head>
<body>
<main class="sheet">

  <section class="card card--front" aria-label="Business card front">
    <div class="front-pattern" role="img" aria-label="Faint repeating pattern of cleaning supplies: spray bottles, sponges, gloves and vacuum cleaners"></div>
    <div class="front-wordmark">
      <span class="name">PKR Tidy Homes</span>
      <span class="suffix">Limited</span>
    </div>
  </section>

  <section class="card card--back" aria-label="Business card back">
    <svg class="back-shape" viewBox="0 0 736 426" preserveAspectRatio="none" aria-hidden="true">
      <path d="M0 0 H212 C292 42 322 150 314 240 L324 262 L309 270 C298 320 276 354 240 376 H736 V426 H0 Z"/>
    </svg>

    <div class="back-wordmark">
      <span class="name">PKR Tidy Homes</span>
      <span class="suffix">Limited</span>
    </div>

    <h2 class="get-in-touch">GET IN TOUCH</h2>

    <ul class="services" aria-label="Services">
      <li>End of Tenancy</li>
      <li>Carpet &amp; Upholstery</li>
      <li>Regular &amp; One Off</li>
      <li class="insured">All work fully insured</li>
    </ul>

    <ul class="contact-list">
      <li class="contact-phone">0800 529 6081</li>
      <li class="contact-mobile">07438 915 702</li>
      <li class="contact-email">Email: pkrtidy@mailbox-demo.co.uk</li>
    </ul>

    <p class="website">www.pkrtidyhomes.co.uk</p>
  </section>

</main>
</body>
</html>
```